Breezeway Climate Business Card Design

Design new, 2 sides, business cards for a residential and light commercial heating, air conditioning contractor.

Target Market(s)

Homeowners, small businesses

Industry/Entity Type

Business

Contact Information for Business Card

Dominic Vasquerelli
Phone - 555-214-6837
Email
Address - PO box 618
Millbrook NJ 07999
Website - www.BreezewayClimateLLC.example

Requirements
Must have
• logo, company colors, standard size with no die cut, so I can use printhaven

```html
<!DOCTYPE html>
<html lang="en">
<head>
<meta charset="utf-8">
<title>Breezeway Climate Business Card</title>
<link href="https://fonts.googleapis.com/css2?family=Arimo:wght@400;700&display=swap" rel="stylesheet">
<style>
  :root {
    --maroon: #9c1c35;
    --orange: #f29a1f;
    --ink: #2a2a2a;
    --paper: #ffffff;
    --stage: #e9e6e1;
    --on-maroon: #ffffff;
  }
  * { box-sizing: border-box; margin: 0; padding: 0; }
  html, body {
    width: 1200px; height: 950px; overflow: hidden;
    background: var(--stage);
    font-family: "Arimo", Arial, sans-serif;
  }
  .canvas {
    position: relative; width: 1200px; height: 950px;
    display: flex; flex-direction: column; align-items: center; justify-content: center; gap: 34px;
  }
  .card {
    position: relative; width: 760px; height: 434px;
    background: var(--paper);
    box-shadow: 0 6px 18px rgba(0,0,0,.18);
    overflow: hidden;
  }
  .brand {
    position: absolute; display: flex; align-items: center; gap: 14px;
    color: var(--maroon); font-weight: 700; white-space: nowrap;
  }
  .brand-dot { border-radius: 50%; background: var(--orange); flex: none; }
  .card-front .brand { left: 50%; top: 50%; transform: translate(-50%, -50%); font-size: 52px; }
  .card-front .brand-dot { width: 40px; height: 40px; }
  .card-back .brand { left: 300px; top: 62px; font-size: 36px; gap: 10px; }
  .card-back .brand-dot { width: 28px; height: 28px; }
  .back-shape { position: absolute; inset: 0; }
  .contact-list {
    position: absolute; left: 36px; top: 150px; list-style: none;
    color: var(--on-maroon); font-size: 19px; line-height: 30px;
  }
  .contact-list li { display: flex; align-items: center; gap: 12px; white-space: nowrap; }
  .contact-list svg { width: 18px; height: 18px; fill: var(--on-maroon); flex: none; }
  .person {
    position: absolute; right: 40px; top: 300px; text-align: right;
    color: var(--on-maroon);
  }
  .person-name { font-size: 28px; font-weight: 700; letter-spacing: .5px; white-space: nowrap; }
  .person-title { font-size: 20px; letter-spacing: 1px; margin-top: 2px; }
  .person-address { font-size: 19px; line-height: 26px; margin-top: 12px; }
</style>
</head>
<body>
<main class="canvas">

  <section class="card card-front" aria-label="Card front">
    <div class="brand"><span class="brand-dot"></span>Breezeway Climate</div>
  </section>

  <section class="card card-back" aria-label="Card back">
    <svg class="back-shape" viewBox="0 0 760 434" preserveAspectRatio="none" aria-hidden="true">
      <path d="M0,100 C250,118 500,190 760,252" fill="none" stroke="var(--ink)" stroke-width="3"/>
      <path d="M0,108 C250,126 500,198 760,260 L760,276 C500,214 250,142 0,124 Z" fill="var(--orange)"/>
      <path d="M0,124 C250,142 500,214 760,276 L760,434 L0,434 Z" fill="var(--maroon)"/>
    </svg>

    <div class="brand"><span class="brand-dot"></span>Breezeway Climate</div>

    <ul class="contact-list">
      <li>
        <svg viewBox="0 0 24 24"><path d="M6.6 10.8a15 15 0 0 0 6.6 6.6l2.2-2.2a1 1 0 0 1 1-.25 11.4 11.4 0 0 0 3.6.57 1 1 0 0 1 1 1V20a1 1 0 0 1-1 1A17 17 0 0 1 3 4a1 1 0 0 1 1-1h3.5a1 1 0 0 1 1 1c0 1.25.2 2.45.57 3.57a1 1 0 0 1-.25 1z"/></svg>
        555-214-6837
      </li>
      <li>
        <svg viewBox="0 0 24 24"><path d="M6 2h12v6H6z M3 9h18v9h-3v4H6v-4H3z M8 15v5h8v-5z"/></svg>
        555-301-4482
      </li>
      <li>
        <svg viewBox="0 0 24 24"><path d="M7 1h10a2 2 0 0 1 2 2v18a2 2 0 0 1-2 2H7a2 2 0 0 1-2-2V3a2 2 0 0 1 2-2zm0 3v14h10V4zm5 15.5a1.2 1.2 0 1 0 0 2.4 1.2 1.2 0 0 0 0-2.4z"/></svg>
        555-987-1203
      </li>
      <li>
        <svg viewBox="0 0 24 24"><path d="M2 5h20v14H2z M3.5 6.5 12 13l8.5-6.5" stroke="var(--maroon)" stroke-width="1.5"/></svg>
        dominic@breezewayclimate.example
      </li>
      <li>
        <svg viewBox="0 0 24 24"><path d="M12 2a10 10 0 1 0 0 20 10 10 0 0 0 0-20zm0 2.2c1 0 2.2 2 2.6 5.3H9.4C9.8 6.2 11 4.2 12 4.2zm-7.6 7.3h3c0 1 .1 2 .3 3H5a7.8 7.8 0 0 1-.6-3zm11.1 0h3a7.8 7.8 0 0 1-.5 3h-2.8c.2-1 .3-2 .3-3zM12 19.8c-1 0-2.1-1.7-2.5-4.3h5c-.4 2.6-1.5 4.3-2.5 4.3z"/></svg>
        www.BreezewayClimateLLC.example
      </li>
    </ul>

    <div class="person">
      <p class="person-name">DOMINIC VASQUERELLI</p>
      <p class="person-title">PRESIDENT</p>
      <p class="person-address">PO box 618<br>Millbrook NJ 07999</p>
    </div>
  </section>

</main>
</body>
</html>
```